KR landing page for e-commerce site

I need to create a landing page design for my website using a wordpress theme. This is a startup company mainly e-commerce. The site mainly serves the needs of those using 3D printers. Think 3D Engineering and tools. Also included :
- Powerpoint master template: information to be presented on the front end of my e-commerce site.
- images as inspiration for header images.
- icon legend and associated images which could be incorporated into the design.
- logo images

This should be a fun site. think engineering, Zorbix-esq, think tank, services. One of the main customer verticals which we are serving is dentistry.

Target Market(s)

3D printer owners. One type of owner is dentists.

Number of Pages Required

3 page

Font styles to use
Sans Serif

Requirements
Must have
• - Use my icons presented
- Theme should be able to be easily updated to plinvora.com
- logo use
- tool imagery
Nice to have
• - 3D Pinter image
- Wheelchair image
- Website coding

```html
<!DOCTYPE html>
<html lang="en">
<head>
<meta charset="utf-8">
<title>Quillark — Engineering Tools &amp; 3D Printing</title>
<link rel="stylesheet" href="https://fonts.googleapis.com/css2?family=Montserrat:wght@300;400;500;600;700;800&family=Raleway:wght@300;400;500&display=swap">
<style>
  :root{
    --ink:#333a44;
    --muted:#555b66;
    --brand-blue:#0070c0;
    --brand-navy:#2d4a9a;
    --brand-violet:#8a2a8c;
    --accent-red:#e0452a;
    --band-blue:#3f80c2;
    --band-deep:#2f6fb3;
    --paper:#ffffff;
    --mist:#efefef;
    --footer:#1d2130;
    --footer-deep:#15171f;
    --field:#ffffff;
    --sign:#e9eefa;
  }
  *{box-sizing:border-box;margin:0;padding:0}
  html,body{width:1200px;height:3851px;overflow:hidden}
  body{position:relative;background:var(--paper);font-family:"Montserrat",sans-serif;color:var(--ink)}
  .abs{position:absolute}

  /* header */
  .site-header{position:absolute;left:0;top:0;width:1200px;height:90px;background:var(--paper)}
  .brand{position:absolute;display:flex;align-items:center;gap:12px;font-family:"Montserrat",sans-serif;font-weight:600;color:var(--brand-navy)}
  .brand-dot{width:34px;height:34px;border-radius:50%;background:var(--brand-violet)}
  .site-header .brand{left:68px;top:22px;font-size:40px;letter-spacing:-0.5px}
  .main-nav{position:absolute;left:531px;top:38px;display:flex;gap:24px;font-size:12.5px;font-weight:500;color:#444}
  .header-phone{position:absolute;left:980px;top:33px;font-size:20px;font-weight:700;color:var(--brand-navy)}

  /* hero */
  .hero-photo{position:absolute;left:0;top:90px;width:1200px;height:630px;
    background:radial-gradient(ellipse at 70% 35%,#6b83a6 0%,#3e5677 45%,#253850 100%)}
  .hero-sign{position:absolute;left:0;top:262px;width:1200px;justify-content:center;gap:26px;font-size:112px;font-weight:600;color:var(--sign);letter-spacing:-2px;line-height:1}
  .hero-sign .brand-dot{width:110px;height:110px}
  .hero-curve{position:absolute;left:0;top:660px}

  /* about */
  .about{position:absolute;left:0;top:714px;width:1200px;height:501px;background:var(--mist)}
  .about-photo{position:absolute;left:115px;top:759px;width:428px;height:404px;
    background:linear-gradient(135deg,#5a4b6e 0%,#2d5a5a 45%,#8a4a5a 100%)}
  .eyebrow{font-family:"Raleway",sans-serif;font-weight:400;color:var(--ink);font-size:21px;line-height:1}
  .section-title{font-family:"Raleway",sans-serif;font-weight:400;color:var(--ink);font-size:34px;line-height:1}
  .title-bar{position:absolute;width:3px;background:var(--accent-red)}
  .body-copy{font-size:11.6px;line-height:20.5px;color:var(--muted);font-weight:400}
  .justify{text-align:justify}
  .btn-more{position:absolute;height:42px;width:163px;background:var(--brand-blue);color:#fff;font-size:15px;font-weight:500;display:flex;align-items:center}
  .btn-more .chev{width:36px;height:42px;display:flex;align-items:center;justify-content:center;border-right:1px solid rgba(255,255,255,.25);margin-right:20px}

  /* products */
  .products-title{position:absolute;left:0;width:1200px;text-align:center;font-family:"Raleway",sans-serif;font-weight:400}
  .rule{position:absolute;height:2px;background:var(--brand-blue)}
  .product-feature-art{position:absolute;left:434px;top:1396px;width:348px;height:389px;
    background:linear-gradient(180deg,#f3e6f1 0%,#e6e4f4 50%,#dcebfa 100%)}
  .feature{position:absolute;font-family:"Raleway",sans-serif;font-size:19px;line-height:21px;color:#444}
  .feature.left{text-align:right;width:300px;left:100px}
  .feature.right{left:819px;width:300px}
  .feature-icon{position:absolute;width:50px;height:50px}

  /* shop band */
  .shop-band{position:absolute;left:0;top:1785px;width:1200px;height:243px;
    background:linear-gradient(90deg,var(--band-deep),var(--band-blue) 50%,var(--band-deep))}
  .shop-band h2{position:absolute;left:91px;top:76px;font-size:30px;font-weight:700;color:#fff;letter-spacing:.2px}
  .shop-band p{position:absolute;left:94px;top:122px;width:650px;font-size:18px;line-height:31px;color:#fff;font-weight:300}
  .shop-band p strong{font-weight:600}
  .btn-outline{position:absolute;left:834px;top:111px;width:196px;height:38px;border:2px solid #fff;color:#fff;font-size:15px;font-weight:500;display:flex;align-items:center;justify-content:center}

  /* team */
  .team-photo{position:absolute;left:648px;top:2181px;width:420px;height:288px;
    background:linear-gradient(135deg,#3a5fc4 0%,#4a6fd0 60%,#2e4fa8 100%)}

  /* contact */
  .contact-stage{position:absolute;left:42px;top:2756px;width:1114px;height:430px;
    background:linear-gradient(180deg,#fafafa 0%,#f1f1f1 55%,#dcdcdc 100%)}
  .contact-card{position:absolute;top:2800px;width:305px;height:288px;background:#fff;text-align:center}
  .card-line{font-size:17px;font-weight:600;color:#3c3c3c;line-height:31px}
  .card-phone{font-size:26px;font-weight:600;color:#444}
  .get{color:var(--brand-violet);font-weight:600;font-size:20px;line-height:1}
  .connected{color:var(--brand-violet);font-weight:700;font-size:30px;line-height:1.1}
  .social{display:flex;gap:30px;justify-content:center;margin-top:26px}
  .social span{width:38px;height:38px;background:#333}
  .social span.round{border-radius:50%}

  /* register */
  .register{position:absolute;left:0;top:3185px;width:1200px;height:386px;background:var(--brand-blue)}
  .register .kicker{position:absolute;left:102px;top:50px;font-size:11.5px;color:#fff;font-weight:500}
  .register h2{position:absolute;left:100px;top:68px;font-size:28px;font-weight:700;color:#fff}
  .register .bar{position:absolute;left:87px;top:48px;width:3px;height:50px;background:#fff}
  .field{position:absolute;background:var(--field);font-size:13px;color:#8a8a8a;padding:0 12px;display:flex;align-items:center}
  .field.area{align-items:flex-start;padding-top:12px}
  .btn-submit{position:absolute;left:961px;top:296px;width:97px;height:36px;border:2px solid #fff;color:#fff;font-size:14px;display:flex;align-items:center;justify-content:center}

  /* footer */
  .site-footer{position:absolute;left:0;top:3571px;width:1200px;height:221px;background:var(--footer)}
  .to-top{position:absolute;left:572px;top:-4px;width:56px;height:56px;border-radius:50%;background:var(--footer);display:flex;align-items:center;justify-content:center}
  .site-footer .brand{left:0;width:1200px;justify-content:center;top:100px;font-size:52px;color:#fff}
  .site-footer .brand-dot{width:40px;height:40px}
  .legal{position:absolute;left:0;top:3792px;width:1200px;height:59px;background:var(--footer-deep);color:#fff;font-size:14px;display:flex;align-items:center;justify-content:center}
</style>
</head>
<body>

<header class="site-header">
  <div class="brand"><span class="brand-dot"></span>quillark</div>
  <nav class="main-nav"><span>HOME</span><span>ABOUT US</span><span>PRODUCTS</span><span>SHOP</span><span>CONTACT</span></nav>
  <div class="header-phone">555.014.2290</div>
</header>

<div class="hero-photo" role="img" aria-label="Office interior with the company name mounted on a wall"></div>
<div class="brand hero-sign"><span class="brand-dot"></span>quillark</div>
<svg class="hero-curve" width="1200" height="60" viewBox="0 0 1200 60" aria-hidden="true">
  <path d="M0 22 Q600 80 1200 0 L1200 60 L0 60 Z" fill="#efefef"/>
</svg>

<section class="about"></section>
<div class="about-photo" role="img" aria-label="Engineer probing a circuit board with multimeter leads"></div>
<span class="title-bar" style="left:630px;top:786px;height:56px"></span>
<div class="abs eyebrow" style="left:644px;top:780px">About our company</div>
<div class="abs section-title" style="left:644px;top:808px">Who We Are?</div>
<p class="abs body-copy justify" style="left:630px;top:876px;width:474px">Quillark is a no-nonsense equipment firm founded to engage and aide customers in adopting and implementing existing and cutting-edge technologies and services. Founded in 2020, Quillark.com is staffed by a team of engineers, sales, and marketing professionals.</p>
<p class="abs body-copy" style="left:630px;top:979px;width:474px">Atlanta being the technology center of the south, it is teaming with technical schools. When possible, we like to engage exceptional technical students in our equipment solutioning. – yes, we believe in giving back.</p>
<div class="btn-more" style="left:630px;top:1064px"><span class="chev"><svg width="12" height="18" viewBox="0 0 12 18"><path d="M2 2 L10 9 L2 16" stroke="#fff" stroke-width="2.4" fill="none"/></svg></span>READ MORE</div>

<section>
  <h2 class="products-title" style="top:1290px;font-size:35px;color:#444">PRODUCTS</h2>
  <p class="products-title" style="top:1333px;font-size:21px;color:#444">Discover the next technologies, frameworks, solutions and services</p>
  <span class="rule" style="left:576px;top:1366px;width:48px"></span>
  <div class="product-feature-art" role="img" aria-label="Large decorative brand emblem in magenta and blue"></div>

  <svg class="feature-icon" style="left:350px;top:1416px" viewBox="0 0 50 50" aria-hidden="true"><rect x="6" y="6" width="38" height="38" rx="6" fill="none" stroke="#1e88d6" stroke-width="2.5"/></svg>
  <div class="feature left" style="top:1474px">Products for those with<br>accessibility needs</div>
  <svg class="feature-icon" style="left:350px;top:1548px" viewBox="0 0 50 50" aria-hidden="true"><rect x="3" y="3" width="44" height="44" rx="3" fill="none" stroke="#b0246f" stroke-width="2.5"/><line x1="3" y1="14" x2="47" y2="14" stroke="#b0246f" stroke-width="2.5"/></svg>
  <div class="feature left" style="top:1609px">3D Printers and<br>Consumables</div>
  <svg class="feature-icon" style="left:342px;top:1683px" viewBox="0 0 58 50" aria-hidden="true"><rect x="3" y="12" width="30" height="32" fill="none" stroke="#444" stroke-width="2.5"/><circle cx="45" cy="28" r="10" fill="none" stroke="#444" stroke-width="2.5"/></svg>
  <div class="feature left" style="top:1741px">Consumables</div>

  <svg class="feature-icon" style="left:818px;top:1414px" viewBox="0 0 50 50" aria-hidden="true"><circle cx="25" cy="25" r="20" fill="none" stroke="#1e88d6" stroke-width="2.5"/></svg>
  <div class="feature right" style="top:1474px">Product Development</div>
  <svg class="feature-icon" style="left:818px;top:1546px" viewBox="0 0 50 50" aria-hidden="true"><rect x="3" y="3" width="44" height="44" rx="3" fill="none" stroke="#b0246f" stroke-width="2.5"/><rect x="15" y="15" width="20" height="20" fill="none" stroke="#b0246f" stroke-width="2.5"/></svg>
  <div class="feature right" style="top:1613px">Tech Consulting</div>
  <svg class="feature-icon" style="left:818px;top:1672px" viewBox="0 0 50 50" aria-hidden="true"><line x1="3" y1="8" x2="47" y2="8" stroke="#444" stroke-width="2.5"/><rect x="18" y="12" width="14" height="14" fill="none" stroke="#444" stroke-width="2.5"/><line x1="5" y1="40" x2="45" y2="40" stroke="#444" stroke-width="2.5"/></svg>
  <div class="feature right" style="top:1733px">Quillark Creations</div>
</section>

<section class="shop-band">
  <h2>ORIGINAL QUILLARK PRODUCTS</h2>
  <p>You are now entering our e-commerce site which displays only products which are designed and produced by <strong>Quillark</strong></p>
  <div class="btn-outline">SHOP NOW</div>
</section>

<section>
  <span class="title-bar" style="left:103px;top:2202px;height:56px"></span>
  <div class="abs eyebrow" style="left:118px;top:2201px;font-size:19px">About Our Team</div>
  <div class="abs section-title" style="left:116px;top:2222px;font-size:36px;letter-spacing:1px">J. ARDENNE</div>
  <p class="abs body-copy" style="left:102px;top:2283px;width:450px">Experienced Technical Consultant and Strategist with a successful track record in client, solution and business development. Proficient in identifying and delivering application and hardware solutions to both business and technical needs.</p>
  <p class="abs body-copy" style="left:102px;top:2386px;width:450px">Innovative engineer and strategist with proven ability to provide technical and sales presentations to clients of all levels, typically within fortune 500 companies.</p>
  <div class="btn-more" style="left:103px;top:2473px"><span class="chev"><svg width="12" height="18" viewBox="0 0 12 18"><path d="M2 2 L10 9 L2 16" stroke="#fff" stroke-width="2.4" fill="none"/></svg></span>READ MORE</div>
  <div class="team-photo" role="img" aria-label="Portrait of the lead consultant against a blue backdrop"></div>
</section>

<section>
  <h2 class="products-title" style="top:2697px;font-size:31px;color:#444">CONTACT INFO</h2>
  <span class="rule" style="left:573px;top:2747px;width:54px"></span>
  <div class="contact-stage" role="img" aria-label="Pale city skyline silhouette"></div>

  <div class="contact-card" style="left:127px">
    <svg style="margin-top:64px" width="92" height="62" viewBox="0 0 92 62" aria-hidden="true"><rect x="3" y="3" width="86" height="56" rx="3" fill="none" stroke="#8a2a8c" stroke-width="5"/><path d="M3 5 L46 38 L89 5 M3 57 L34 30 M89 57 L58 30" fill="none" stroke="#8a2a8c" stroke-width="4"/></svg>
    <div class="card-line" style="margin-top:22px">info@Quillark.com<br>sales@Quillark.com</div>
  </div>
  <div class="contact-card" style="left:450px">
    <svg style="margin-top:54px" width="76" height="76" viewBox="0 0 76 76" aria-hidden="true"><circle cx="38" cy="38" r="34" fill="none" stroke="#8a2a8c" stroke-width="4"/><path d="M24 18 C18 22 18 32 26 44 C34 56 44 60 52 56 L48 46 L40 48 C36 44 32 38 30 32 L36 28 Z" fill="#8a2a8c"/></svg>
    <div class="card-phone" style="margin-top:36px">555.014.2290</div>
  </div>
  <div class="contact-card" style="left:772px">
    <div class="get" style="margin-top:78px">GET</div>
    <div class="connected">CONNECTED</div>
    <div class="social"><span></span><span></span><span class="round"></span></div>
  </div>
</section>

<section class="register">
  <span class="bar"></span>
  <div class="kicker">THE BESTPLACE TO FIND THE HOUSE YOU WANT</div>
  <h2>REGISTER YOUR INTEREST</h2>
  <div class="field" style="left:117px;top:117px;width:448px;height:39px">NAME</div>
  <div class="field" style="left:117px;top:180px;width:448px;height:40px">TELEPHONE</div>
  <div class="field" style="left:117px;top:244px;width:448px;height:39px">EMAIL</div>
  <div class="field area" style="left:581px;top:117px;width:477px;height:166px">MESSAGE</div>
  <div class="btn-submit">SUBMIT</div>
</section>

<footer class="site-footer">
  <div class="to-top"><svg width="20" height="12" viewBox="0 0 20 12" aria-hidden="true"><path d="M2 10 L10 2 L18 10" stroke="#fff" stroke-width="2.2" fill="none"/></svg></div>
  <div class="brand"><span class="brand-dot"></span>quillark</div>
</footer>
<div class="legal">Copyright© 2020 &nbsp;| All Right Reserved</div>

</body>
</html>
```